Breakfast Cafe - The Sunny Perch

It is for my breakfast and lunch cafe with a hawaiian / beach theme. I am open 7 days a week from 7am to 2pm. We serve traditional American food such as omelettes, pancakes, burgers and sandwiches. I'll upload my old card and my new logo to be used. We have a lot of day to day regulars who eat there during the week, our t-shirts actually say 'Locals Only' on them. Hope this helps. Thanks.

Target Market(s)

anyone who has an appetite!

Industry/Entity Type

American Restaurant

Contact Information for Business Card

7340D Marlin Harbor Road
Long Beach, California
(555) 317-2286

Requirements
Must have
• Address and phone number easily readable.
Nice to have
• beach or tropical theme

```html
<!DOCTYPE html>
<html lang="en">
<head>
<meta charset="utf-8">
<title>The Sunny Perch – Business Card</title>
<link rel="stylesheet" href="https://fonts.googleapis.com/css2?family=Delius&family=Gochi+Hand&family=Dancing+Script:wght@500&display=swap">
<style>
  :root {
    --mint-light: #eef8f1;
    --mint: #bfe6cf;
    --mint-deep: #8fd1ab;
    --palm: #4fb683;
    --band: #129a62;
    --ink: #141414;
    --sun: #f4a63a;
    --wood: #a0622a;
    --sea-blue: #3cb0d8;
    --rust: #b4652b;
    --white: #ffffff;
  }
  * { margin: 0; padding: 0; box-sizing: border-box; }
  html, body { width: 720px; height: 1200px; overflow: hidden; background: var(--white); }
  .card {
    position: relative;
    width: 720px;
    height: 1200px;
    overflow: hidden;
    background:
      radial-gradient(ellipse 60% 35% at 30% 20%, rgba(255,255,255,.7), transparent 70%),
      radial-gradient(ellipse 50% 30% at 85% 45%, rgba(255,255,255,.5), transparent 70%),
      linear-gradient(180deg, var(--mint-light) 0%, var(--mint) 45%, var(--mint-deep) 85%);
  }
  .palm-grove {
    position: absolute;
    left: 0; top: 570px;
    width: 720px; height: 460px;
    background:
      radial-gradient(ellipse 22% 30% at 12% 18%, rgba(79,182,131,.55), transparent 70%),
      radial-gradient(ellipse 22% 30% at 88% 18%, rgba(79,182,131,.55), transparent 70%),
      radial-gradient(ellipse 30% 40% at 8% 70%, rgba(79,182,131,.5), transparent 70%),
      radial-gradient(ellipse 30% 40% at 92% 70%, rgba(79,182,131,.5), transparent 70%),
      linear-gradient(180deg, rgba(143,209,171,0) 0%, rgba(79,182,131,.45) 100%);
  }
  .brand {
    position: absolute;
    left: 0; top: 110px;
    width: 720px;
    text-align: center;
  }
  .brand-dot {
    display: block;
    width: 300px; height: 300px;
    margin: 0 auto 28px;
    border-radius: 50%;
    background: var(--sun);
    border: 18px solid var(--wood);
  }
  .brand-name {
    font-family: "Delius", sans-serif;
    font-weight: 400;
    font-size: 70px;
    line-height: 1;
    color: var(--sea-blue);
  }
  .brand-city {
    margin-top: 22px;
    font-family: "Delius", sans-serif;
    font-size: 24px;
    letter-spacing: 7px;
    color: var(--rust);
  }
  .hours {
    position: absolute;
    left: 0; top: 690px;
    width: 720px;
    text-align: center;
    font-family: "Gochi Hand", cursive;
    font-size: 44px;
    color: var(--ink);
    letter-spacing: 1px;
  }
  .contact {
    position: absolute;
    left: 0; top: 795px;
    width: 720px;
    text-align: center;
    font-family: "Delius", sans-serif;
    font-size: 40px;
    line-height: 62px;
    color: var(--ink);
    font-style: normal;
  }
  .footer-band {
    position: absolute;
    left: 0; top: 1029px;
    width: 720px; height: 171px;
    background: var(--band);
  }
  .tagline {
    position: absolute;
    left: 0; top: 1042px;
    width: 720px;
    text-align: center;
    font-family: "Dancing Script", cursive;
    font-weight: 500;
    font-size: 50px;
    letter-spacing: 2px;
    color: var(--white);
  }
</style>
</head>
<body>
  <main class="card">
    <div class="palm-grove" role="img" aria-label="Silhouettes of palm trees in soft green"></div>

    <header class="brand">
      <span class="brand-dot"></span>
      <h1 class="brand-name">The Sunny Perch</h1>
      <p class="brand-city">LONG BEACH, CA</p>
    </header>

    <p class="hours">OPEN DAILY FROM 7AM-2PM</p>

    <address class="contact">
      <div class="contact-phone">Phone: (555) 317-2286</div>
      <div class="contact-street">7340D Marlin Harbor Road</div>
      <div class="contact-city">Long Beach, California</div>
    </address>

    <div class="footer-band"></div>
    <p class="tagline">Family owned &amp; operated</p>
  </main>
</body>
</html>
```